Brochure & Business card design

Looking for a new business card design i want it to be modern and sharp looking i usually order plastic business cards, and i would like to make the colors like the logo teal/charcoal i will like to have our services on icons with words.... our services are
ROOFING GUTTERS PAINTING PRESSURE WASHING EXTERIOR DESIGN & ATTIC VENTILATION. I also want to add my credentials

Target Market(s)

Oregon local market

Industry/Entity Type

Residential Construction

Contact Information for Business Card

Business info, services, number, website

Font styles to use
Serif
Sans Serif

Colors
33b8a4
5c5c5c
ffffff

Requirements
Must have
• Tomas Relke
• Cell:
• Office:
• Email:
• Website:
• also i need our social media icons
• Services ROOFING GUTTERS PAINTING PRESSURE WASHING EXTERIOR DESIGN & ATTIC VENTILATION
• -icons for number, web, email, cell
• OR #384152
• Wa #KTRAPLD547Q3
Nice to have
• -Clean design Front & Back
• -Icons
• -shape House just like logo design
• -First Impression
Should not have
• Not Busy or lost of eye contact

```html
<!DOCTYPE html>
<html lang="en">
<head>
<meta charset="utf-8">
<title>Cedarline Exteriors — Business Card</title>
<link rel="stylesheet" href="https://fonts.googleapis.com/css2?family=Libre+Baskerville:wght@400;700&family=Roboto:wght@400&display=swap">
<style>
  :root {
    --teal: #1b9787;
    --charcoal: #1f1f1f;
    --slate: #555558;
    --text-grey: #4d4d4f;
    --white: #ffffff;
    --backdrop: #e4e4e4;
  }
  * { margin: 0; padding: 0; box-sizing: border-box; }
  html, body { width: 1125px; height: 1200px; overflow: hidden; background: var(--backdrop); }
  .stage {
    position: relative; width: 1090px; height: 1163px;
    transform: scale(1.0321); transform-origin: 0 0;
  }
  .card { position: absolute; left: 166px; width: 800px; height: 457px; }
  .card--front { top: 103px; background: var(--charcoal); }
  .card--back { top: 619px; background: var(--white); }

  .tab {
    position: absolute; left: 0; width: 75px; height: 47px;
    border-radius: 0 24px 24px 0; display: flex; align-items: center; justify-content: flex-end; padding-right: 13px;
  }
  .tab--teal { background: var(--teal); }
  .tab--grey { background: var(--slate); }
  .tab svg { width: 26px; height: 26px; fill: var(--white); }

  .holder-name {
    position: absolute; left: 98px; top: 56px;
    font: 700 27px/1 "Libre Baskerville", serif; color: var(--teal); letter-spacing: 0.5px;
  }
  .holder-title {
    position: absolute; left: 98px; top: 93px;
    font: 700 17px/1 "Libre Baskerville", serif; color: var(--white);
  }
  .contact-line {
    position: absolute; left: 99px;
    font: 400 19px/24px "Roboto", sans-serif; color: var(--white);
  }

  .brand-front {
    position: absolute; left: 494px; top: 210px; width: 240px; text-align: center;
  }
  .brand-front .brand-mark { width: 22px; height: 22px; background: var(--teal); margin: 0 auto 14px; }
  .brand-front .brand-name {
    font: 700 26px/1.15 "Libre Baskerville", serif; color: var(--teal); letter-spacing: 0.5px;
  }
  .tagline {
    margin-top: 8px; padding-top: 6px; border-top: 1px solid var(--slate);
    font: 400 13px/1 "Libre Baskerville", serif; color: var(--slate); letter-spacing: 1.2px;
  }

  .licence {
    position: absolute; top: 30px;
    font: 400 19px/1 "Roboto", sans-serif; color: var(--text-grey);
  }
  .licence--wa { left: 42px; }
  .licence--or { right: 41px; }

  .brand-back { position: absolute; left: 0; right: 0; top: 112px; text-align: center; }
  .brand-back .brand-mark { width: 30px; height: 30px; background: var(--teal); margin: 0 auto 18px; }
  .brand-back .brand-name {
    font: 700 40px/1.15 "Libre Baskerville", serif; color: var(--teal); letter-spacing: 1px;
  }

  .badge { position: absolute; }
  .badge--left { left: 24px; top: 374px; width: 126px; height: 48px; background: #d0d0d2; border-radius: 2px; }
  .badge--right { left: 665px; top: 380px; width: 111px; height: 42px; background: #111; border-radius: 5px; }

  .services {
    position: absolute; left: 160px; width: 494px; top: 378px; text-align: center;
    font: 400 19px/24px "Roboto", sans-serif; color: var(--text-grey); letter-spacing: 0.2px;
  }
  .services .sep {
    display: inline-block; width: 8px; height: 8px; background: var(--teal);
    margin: 0 5px; vertical-align: 3px;
  }
</style>
</head>
<body>
<div class="stage">

  <section class="card card--front" aria-label="Business card front">
    <div class="tab tab--teal" style="top:59px">
      <svg viewBox="0 0 24 24"><circle cx="12" cy="7.5" r="4.5"/><path d="M3 21c0-5 4-8 9-8s9 3 9 8z"/></svg>
    </div>
    <h1 class="holder-name">TOMAS RELKE</h1>
    <p class="holder-title">CEO/FOUNDER</p>

    <div class="tab tab--grey" style="top:205px">
      <svg viewBox="0 0 24 24"><path d="M12 2a7 7 0 0 0-7 7c0 5 7 13 7 13s7-8 7-13a7 7 0 0 0-7-7zm0 9.5A2.5 2.5 0 1 1 12 6.5a2.5 2.5 0 0 1 0 5z"/></svg>
    </div>
    <p class="contact-line" style="top:208px">4821 Alder Crest Road<br>Salem, Oregon 97301</p>

    <div class="tab tab--teal" style="top:286px">
      <svg viewBox="0 0 24 24"><path d="M7 1.5h10a1.5 1.5 0 0 1 1.5 1.5v18a1.5 1.5 0 0 1-1.5 1.5H7A1.5 1.5 0 0 1 5.5 21V3A1.5 1.5 0 0 1 7 1.5zm0.5 3v14h9v-14zm3 15.5v1h3v-1z"/></svg>
    </div>
    <p class="contact-line" style="top:296px">503-555-0148</p>

    <div class="tab tab--grey" style="top:349px">
      <svg viewBox="0 0 24 24"><circle cx="12" cy="12" r="10"/><path d="M7 6c2 1 2 3 4 3s1 3 3 3-1 4 1 5M15 4c0 2 2 2 3 4M5 15c2 0 3 1 3 3" stroke="#555558" stroke-width="2" fill="none"/></svg>
    </div>
    <p class="contact-line" style="top:344px">cedarlineexteriors.com<br>CedarlineExteriors.com</p>

    <div class="brand-front">
      <div class="brand-mark"></div>
      <p class="brand-name">CEDARLINE<br>EXTERIORS</p>
      <p class="tagline">WHEN QUALITY MATTERS</p>
    </div>
  </section>

  <section class="card card--back" aria-label="Business card back">
    <p class="licence licence--wa">Wa #KTRAPLD547Q3</p>
    <p class="licence licence--or">OR #384152</p>

    <div class="brand-back">
      <div class="brand-mark"></div>
      <p class="brand-name">CEDARLINE<br>EXTERIORS</p>
    </div>

    <div class="badge badge--left" role="img" aria-label="Roofing contractor certification badge"></div>
    <p class="services">ROOFING<span class="sep"></span>GUTTERS<span class="sep"></span>PAINTING<span class="sep"></span>PRESSURE<br>WASHING&nbsp; EXTERIOR DESIGN &amp; ATTIC VENTILATION</p>
    <div class="badge badge--right" role="img" aria-label="Accredited business badge"></div>
  </section>

</div>
</body>
</html>
```